Bottled Margarita Label Project

We need a label design (using a 750 ml bottle) for an all natural, premium, Ready to Drink (as in pre-mixed) Margarita. The brand is called VONDRA Pure Margarita. We were tired of the chemical, sugary, preservative laden "margaritas" with artificial colorings and cheap tequilas, so we developed a simple, straightforward CLASSIC, ingredient driven margarita made with only the purest, traditional ingredients: 100% Blue Agave Tequila Reposado, Double Distilled Orange Liqueur, Lime Juice and sweetened with Organic Cane Sugar. The result is a pure margarita, the kind you got on that amazing beach vacation in Mexico. This is a product that can be chilled and served over ice or straight up. You might grab one to take to a BBQ or to the beach. It's simple, sexy and classic. We are hoping the final design can communicate purity, integrity of ingredients and the freedom one might feel when on vacation in the sun. This doesnt have to be a Latin themed beverage, but more of a Summer / chill / "sala del oro" in a bottle vibe. Thank you!

Target Market(s)

25 to 45 year olds who feel they know what makes up a good margarita. Aspirational types who love adventurous vacations but are not necessarily wealthy. Our customer doesn't always have the time to make a real margarita from scratch but wish they could get a decent one in a bottle that doesn't taste artificial. They are brand and label conscious and will pay a little more for quality as long as there is value.

Industry/Entity Type

Cafe

Requirements
Must have
• Must have "Vondra" and "pure margartia" clearly listed as the name of the beverage. Must also make clear that this is "Premium", "Ready to Drink" and "Made with 100% Blue Agave Tequila"
Nice to have
• We really love designs that are clean and uncluttered. We have imagined a clear 750ml bottle. Think about tequila when you think about this label. This is a hand made, artisan product produced in batches. We are looking for a finished label/bottle that is colorful, transcendent, artisinal and timeless. It should be mature but not stuffy. It should be simple and sexy - not splashy, brash or silly. Our competition is Tidy Moth Margarita, Rafa Tolentes, and Brevo pre-mixed margaritas which are fake margaritas made in huge factories. Vondra is made with integrity and honest ingredients. For colors, greens come to mind but we are totally open to a designer's vision ;). This should be a product that a fashion forward airline like Halcyon Skyways would want serve and a bottle that a savvy drinker would choose over the bland, mainstream brands. Check out Munrez Cachaça for a sexy, vibrant take on a bottle of alcohol with a Summer slant. Also look at Velquiro tequila. They have a wonderful label that blends vintage and modern elements with minimalist design and comes off as handmade.
Should not have
• Elements we do NOTwant to see any red colors, sombreros, parrots, tiki masks, palm trees, spring break, deserted islands, or Dale Hornsby imagery. This should be a product that an airline like Halcyon Skyways would want to serve.

```html
<!DOCTYPE html>
<html lang="en">
<head>
<meta charset="utf-8">
<title>Vondra Pure Margarita – Label</title>
<link rel="stylesheet" href="https://fonts.googleapis.com/css2?family=Poiret+One&family=Cinzel:wght@400&family=Libre+Baskerville&family=Archivo+Narrow&display=swap">
<style>
  :root {
    --backdrop: #2d5a2f;
    --label-paper: #a3a3a1;
    --label-paper-light: #b4b4b2;
    --ink-green: #0e4a2a;
    --ink-dark: #2b2f2b;
    --rule: #1d3b28;
  }
  * { margin: 0; padding: 0; box-sizing: border-box; }
  html, body {
    width: 1200px;
    height: 1000px;
    overflow: hidden;
    background: var(--backdrop);
  }
  .canvas {
    position: relative;
    width: 1200px;
    height: 1000px;
  }
  .label {
    position: absolute;
    left: 395px;
    top: 35px;
    width: 410px;
    height: 930px;
    background: radial-gradient(ellipse at 50% 40%, var(--label-paper-light), var(--label-paper));
    color: var(--ink-green);
    text-align: center;
  }
  .brand-name {
    position: absolute;
    top: 210px;
    left: 0;
    width: 100%;
    font-family: "Poiret One", sans-serif;
    font-size: 118px;
    line-height: 1;
    color: var(--ink-green);
    letter-spacing: -2px;
  }
  .brand-rule {
    position: absolute;
    top: 404px;
    left: 30px;
    width: 350px;
    height: 2px;
    background: var(--rule);
  }
  .product-pure {
    position: absolute;
    top: 452px;
    left: 0;
    width: 100%;
    font-family: "Cinzel", serif;
    font-size: 46px;
    letter-spacing: 22px;
    padding-left: 22px;
    line-height: 1;
    color: var(--ink-green);
  }
  .product-type {
    position: absolute;
    top: 505px;
    left: 0;
    width: 100%;
    font-family: "Cinzel", serif;
    font-size: 25px;
    letter-spacing: 3px;
    line-height: 1;
    color: var(--ink-green);
  }
  .ingredients {
    position: absolute;
    top: 600px;
    left: 24px;
    width: 362px;
    font-family: "Libre Baskerville", serif;
    font-size: 12px;
    line-height: 20px;
    color: var(--ink-dark);
  }
  .grade {
    position: absolute;
    top: 768px;
    left: 0;
    width: 100%;
    font-family: "Archivo Narrow", sans-serif;
    font-size: 25px;
    line-height: 1;
    color: var(--ink-dark);
  }
  .volume {
    position: absolute;
    top: 866px;
    left: 0;
    width: 100%;
    font-family: "Archivo Narrow", sans-serif;
    font-size: 15px;
    line-height: 1;
    color: var(--ink-dark);
  }
  .base-band {
    position: absolute;
    left: 0;
    bottom: 4px;
    width: 100%;
    height: 4px;
    background: var(--ink-green);
  }
</style>
</head>
<body>
  <main class="canvas">
    <section class="label">
      <h1 class="brand-name">vondra</h1>
      <div class="brand-rule"></div>
      <p class="product-pure">PURE</p>
      <p class="product-type">MARGARITA</p>
      <p class="ingredients">Made with only the purest, traditional ingredients: 100% blue agave tequila reposado, double distilled orange liqueur, lime juice and sweetened with organic cane sugar.</p>
      <p class="grade">PREMIUM</p>
      <p class="volume">750 ML</p>
      <div class="base-band"></div>
    </section>
  </main>
</body>
</html>
```